Personal coach needs brochure design for inspirational essay about authenticity

Overview:
I want a beautiful brochure, 11”x17” that folds to 8-1/2”x11” with 4 pages. Think of it as an oversize greeting card.
• Front cover: photograph of a dancer and title with attribution of quote (Lumafold jpeg photo attached)
• Inside spread: Copy (Helena Brisk copy attached) with some appropriate illustration, based on cover photo
• Back cover: contact information, brief descriptive copy, two small photos (jpeg photo attached; see copy for direction)
Copy for front cover title, inside spread and back cover is attached in doc titled "Helena Brisk copy"

Purpose of brochure:
I'm a personal coach and once a year I produce a 4-page illustrated inspirational essay, which invites personal reflection on living a more mindful, meaningful life. Most people I send them to collect them. Someday in the future I'd like to put a collection of these essays into a coffee table book and also create a website for the collection, which is related to the personal coaching that I do.
I have the brochures printed hard copy. I have attached a few examples from previous years. Each has a unique design related to its theme.

Concept:
This year’s essay theme, “There will only ever be one you!” is based on a quote by Helena Brisk, a famous modern dancer. The complete quote, which appears in the copy, is about being true to one’s authentic self. The essay is not about dance, but because the author of the quote was a dancer who personified this theme of being unique to self, I have selected a photo of dance for the cover.

Design Guidance:
Front cover: One possibility is to expand the background color of the Lumafold photo so the photo seems to emerge from the background. But I am open to ideas. I think the photo is artsy enough as it is, but there may be other ways to treat it (e.g. special effects) that would also work. The title should appear somewhere. Make the attribution (--Helena Brisk) in smaller type than the title.

Inside Spread: There may be ways to borrow a design motif from the cover photo to make the inside spread more visually interesting, i.e., not just straight copy. I think it may be helpful to make the font size of the quote larger than the rest of the copy, but it has to be read in sequence. Or maybe it's printed in same size as copy, but then also repeated and displayed by itself in larger type.

Back cover: If you look at some of the other examples I’ve sent, you’ll see how the back cover is typically handled. I want a reduced version of the cover to be placed near the line that says "this is the 16th in a series.." Then, there’s a jpeg photo of Helena Brisk that should be placed next to the copy description of her.

Need extra days to review

```html
<!DOCTYPE html>
<html lang="en">
<head>
<meta charset="utf-8">
<title>There Will Only Ever Be One You – Brochure Spreads</title>
<link href="https://fonts.googleapis.com/css2?family=Anton&family=Great+Vibes&family=Open+Sans:wght@400;600;700&family=Roboto+Condensed:wght@400;700&display=swap" rel="stylesheet">
<style>
  :root {
    --backdrop: #dedede;
    --paper: #ffffff;
    --ink: #1c1c1c;
    --magenta: #c4117e;
    --gold: #f4a10b;
    --night: #0b0b0b;
    --slate: #3c4f66;
    --fold: #e4e4e4;
  }
  * { box-sizing: border-box; margin: 0; padding: 0; }
  html, body { width: 973px; height: 1200px; overflow: hidden; }
  body { background: var(--backdrop); position: relative; font-family: "Open Sans", sans-serif; color: var(--ink); }

  .spread { position: absolute; left: 73px; width: 827px; height: 534px; display: flex; box-shadow: 2px 3px 5px rgba(0,0,0,.25); }
  .spread--outer { top: 29px; }
  .spread--inner { top: 599px; }
  .page { position: relative; width: 50%; height: 100%; background: var(--paper); overflow: hidden; }
  .page--back { border-right: 1px solid var(--fold); }
  .page--dark { background: var(--night); }

  /* Back cover */
  .series-thumb { position: absolute; left: 22px; top: 84px; width: 73px; height: 94px; border: 1px solid #9a9a9a; background: var(--paper); overflow: hidden; }
  .series-thumb__photo { position: absolute; left: 4px; top: 14px; width: 44px; height: 52px; background: linear-gradient(160deg, #6a7a8e, var(--slate)); border-radius: 40% 50% 45% 55%; }
  .series-thumb__title { position: absolute; right: 6px; top: 14px; font-family: "Anton", sans-serif; color: var(--magenta); font-size: 11px; line-height: 9.5px; text-align: right; }
  .series-thumb__you { position: absolute; right: 4px; top: 66px; font-family: "Great Vibes", cursive; color: var(--gold); font-size: 13px; }
  .series-thumb__credit { position: absolute; right: 8px; bottom: 5px; font-size: 2.5px; }

  .series-intro { position: absolute; left: 101px; top: 82px; width: 290px; }
  .series-intro__lead { font-size: 10px; line-height: 11.5px; }
  .series-intro__lead strong { color: var(--magenta); font-weight: 600; }
  .contact { margin-top: 8px; font-size: 7.3px; line-height: 11.4px; }
  .contact b { font-weight: 700; }
  .contact__gap { margin-top: 11px; }

  .portrait { position: absolute; left: 22px; top: 252px; width: 97px; height: 97px; background: radial-gradient(ellipse at 45% 60%, #b9b3a6 0%, #4a4744 35%, #141414 70%); }

  .about { position: absolute; left: 22px; top: 357px; width: 360px; font-family: "Roboto Condensed", sans-serif; }
  .about__heading { font-weight: 700; color: var(--magenta); font-size: 8px; line-height: 10px; letter-spacing: -.1px; }
  .about__text { font-size: 7px; line-height: 9.7px; letter-spacing: -.1px; margin-bottom: 7px; }

  /* Front cover */
  .cover-photo { position: absolute; left: 27px; top: 89px; width: 290px; height: 386px; background: radial-gradient(ellipse at 45% 50%, #4d6179 0%, var(--slate) 40%, rgba(60,79,102,.0) 72%); }
  .cover-title { position: absolute; right: 45px; top: 84px; font-family: "Anton", sans-serif; color: var(--magenta); font-size: 64px; line-height: 53.5px; text-align: right; letter-spacing: -.5px; }
  .cover-you { position: absolute; right: 18px; top: 352px; font-family: "Great Vibes", cursive; color: var(--gold); font-size: 104px; line-height: 1; }
  .cover-credit { position: absolute; right: 45px; top: 486px; font-size: 11.5px; letter-spacing: .3px; }

  /* Inside spread */
  .essay { position: absolute; left: 31px; top: 90px; width: 354px; font-size: 7.6px; line-height: 11.3px; }
  .essay p { margin-bottom: 11px; }
  .essay__quote { color: var(--magenta); font-weight: 600; text-align: center; padding: 12px 12px 0; }

  .portrait-large { position: absolute; inset: 0; background: radial-gradient(ellipse at 58% 40%, #8d8d8d 0%, #3a3a3a 30%, var(--night) 68%); }
  .halo { position: absolute; left: 0; top: 0; }
  .reflection { position: absolute; left: 28px; top: 406px; width: 360px; color: #fff; text-align: center; font-size: 7.4px; line-height: 11.3px; }
  .reflection p { margin-bottom: 11px; }
</style>
</head>
<body>

<section class="spread spread--outer">
  <article class="page page--back">
    <div class="series-thumb" role="img" aria-label="Reduced version of the front cover">
      <div class="series-thumb__photo"></div>
      <div class="series-thumb__title">THERE<br>WILL<br>ONLY<br>EVER<br>BE<br>ONE</div>
      <div class="series-thumb__you">you!</div>
      <div class="series-thumb__credit">Helena Brisk</div>
    </div>

    <div class="series-intro">
      <p class="series-intro__lead"><strong>There Will Only Ever Be One You</strong> is the 16th in a series of Labor Day essays inviting a moment of reflection on living a more meaningful, more mindful life</p>
      <div class="contact">
        <p><b>Nora Velin Ashby,</b> Ph.D.</p>
        <p>Alder Bend House - 12 Orchard Lane</p>
        <p>Fernhill, Massachusetts&nbsp; 01900</p>
        <p class="contact__gap">Mobile:&nbsp; 555-014-2288</p>
        <p>Email: nvashby@fernmail.net</p>
        <p>©2023</p>
      </div>
    </div>

    <div class="portrait" role="img" aria-label="Black and white photograph of Helena Brisk dancing in a flowing white dress"></div>

    <div class="about">
      <h3 class="about__heading">ABOUT HELENA BRISK:</h3>
      <p class="about__text">Born in 1894, Helena Brisk danced and taught for over 70 years.&nbsp; She is recognized as a primal artistic force of the 20th century, whose influence on modernity has been compared to Pell Arden, Jonas Quill, Ivo Strand, and Frederick Lane Wirth.&nbsp; Her themes dealt with the lives and conflicts of ordinary people, and she brought serious issues to the stage like war, poverty, intolerance and the injustices of slavery and treatment of Native Americans. Rebelling against conventions of the past, her dancing and choreography exposed the depths of human emotion through intense movements that were forceful, stark, angular, jagged, and percussive – startlingly unlike the formality of classical ballet, which she saw as antiquated.</p>
      <h3 class="about__heading">ABOUT PHOTOGRAPHER CLARA VOSS:</h3>
      <p class="about__text">In 1935 Clara Voss saw a performance by modern dancer and choreographer Helena Brisk. Voss was so inspired by the dance performance that she introduced herself to Brisk, and the two artists began an artistic collaboration that lasted more than 60 years. Voss often photographed dancers in action, to capture the emotion behind their movement. Her artistic style was in line with Brisk’s philosophy of dance. This photo from the dance, “Letter to the Valley,” is one of Voss’s most famous photographs. The title of this work comes from an Emmeline Darrow poem, which inspired Brisk to create a dance performance based on Darrow’s life.</p>
    </div>
  </article>

  <article class="page page--front">
    <div class="cover-photo" role="img" aria-label="Photograph of a leaping dancer in a flowing blue-grey dress"></div>
    <h1 class="cover-title">THERE<br>WILL<br>ONLY<br>EVER<br>BE<br>ONE</h1>
    <div class="cover-you">you!</div>
    <p class="cover-credit">Helena&nbsp; Brisk</p>
  </article>
</section>

<section class="spread spread--inner">
  <article class="page">
    <div class="essay">
      <p>In the rural Ohio village where I grew up, one of the highlights of Sunday morning church service -- in between congregational hymn-singing and the preacher’s sermon -- was the “special selection,” a musical performance by a parishioner. Typically, it was a vocalist or instrumental on piano, organ or violin. One Sunday, we were surprised by an unusual performance.&nbsp; A plump, buxom farm wife approached the pulpit, puckered up her lips and unexpectedly began to whistle the hymn “The Lantern on the Hill.” As a 10-year-old, I found this hilarious as I tried to choke back my wide-eyed amazement and giggles. Despite the irreverence of my pre-adolescent reaction, this memory has stayed with me for decades as an iconic example of the wonderment of individual differences. Of the delight I find in witnessing someone express herself in sometimes surprising and even courageous ways.&nbsp; Of the marvel of beholding a person be truly authentic and uniquely original.</p>
      <p>Someone who personified the irrepressible impulse to express her individuality was the early 20th century dancer and choreographer Helena Brisk.&nbsp; A pioneer of modern dance, she threw tradition overboard and was inspired to dance in a way that was a radical departure from the formalized style and rigidly dictated forms of classical ballet. Brisk felt compelled to express the rawness and emotion of human experience in her dancing -- not just present a form of pretty entertainment. Iconoclastically brilliant, she created a new language of dance, a revolutionary vocabulary of movement that electrified the stage, often creating a visceral response in the audience.</p>
      <p>In her biography of Brisk, her friend and equally talented choreographer Ada Linholm recalled that despite sensational reviews for her own innovative work in the Broadway musical Prairie Song!, Linholm had a gnawing feeling that her work was only mediocre.&nbsp; Linholm confessed her anxieties to Brisk who listened quietly and then responded, “There will only ever be one you!”&nbsp; Continuing, she added:</p>
      <p class="essay__quote">“There is a vitality, a life-force, an energy, a quickening that is translated through you into action.&nbsp; And because there is only one of you in all of time, this expression is unique.&nbsp; And if you block it, the world will not have it. It is not your business to determine how good it is nor how valuable nor how it compares with other expressions. It is your business to keep it yours clearly and directly, to keep the channel open. You have to keep open and aware directly to the urges that motivate you.&nbsp; Above all else, keep the channel open!”</p>
    </div>
  </article>

  <article class="page page--dark">
    <div class="portrait-large" role="img" aria-label="Black and white photograph of Helena Brisk with eyes closed and hands raised"></div>
    <svg class="halo" width="414" height="534" viewBox="0 0 414 534" aria-hidden="true">
      <circle cx="215" cy="176" r="104" fill="#c4117e" opacity="0.78"/>
    </svg>
    <div class="reflection">
      <p>Brisk’s wisdom reminds us that we must not hold back or judge our gifts.&nbsp; Although there may be moments when we doubt ourselves or when we worry that we’re not good enough, our job is to be fearless and to “keep the channel open.”</p>
      <p>Guard the precious miracle of your own uniqueness.&nbsp; Find that home-sweet-home feeling&nbsp; where you feel you are your most authentic self.&nbsp; There will only ever be one you!&nbsp; And importantly, respect the differences of others.&nbsp; Our world would be a drab, boring place if we all&nbsp; only whistled one tune.</p>
    </div>
  </article>
</section>

</body>
</html>
```